Gilt Corner Shop Sign

Name of company
Gilt Corner
Gilt Corner is a picture framing shop and art gallery selling custom frames, art work and gifts.
Needing a design for shop front sign.

The Sign
The sign is above the shop front window and is approximately 12 feet wide by 43 inches high. White on black. White striped boarder that looks like a picture frame with Gilt Corner in classic lettering including space for a phone number and it may or may not need to include description of services. Something cute in one area like a picture frame with a heart inside. A friendly feel like something that would be special and feels like yours. I have attached a photo of the existing sign to be replaced.

Thank you for your time.

```html
<!DOCTYPE html>
<html lang="en">
<head>
<meta charset="utf-8">
<title>Gilt Corner Shop Sign</title>
<link rel="stylesheet" href="https://fonts.googleapis.com/css2?family=Playfair+Display:wght@400&display=swap">
<style>
  :root {
    --canvas-bg: #dcdcdc;
    --sign-black: #0c0c0c;
    --band-dark: #141210;
    --band-gold: #3a2e14;
    --frame-white: #ffffff;
    --text-white: #ffffff;
  }
  html, body {
    margin: 0;
    padding: 0;
    width: 993px;
    height: 1200px;
    overflow: hidden;
    background: var(--canvas-bg);
  }
  .canvas {
    position: relative;
    width: 993px;
    height: 1200px;
  }
  .sign {
    position: absolute;
    left: 81px;
    top: 477px;
    width: 831px;
    height: 246px;
    border: 1px solid var(--frame-white);
    box-sizing: border-box;
  }
  .sign__pattern-band {
    position: absolute;
    inset: 0;
    background: radial-gradient(ellipse at center, var(--band-gold) 0%, var(--band-dark) 70%);
  }
  .sign__panel {
    position: absolute;
    left: 26px;
    top: 24px;
    right: 26px;
    bottom: 24px;
    background: var(--sign-black);
    border: 3px solid var(--frame-white);
  }
  .sign__name {
    position: absolute;
    left: 0;
    right: 0;
    top: 46px;
    margin: 0;
    text-align: center;
    font-family: "Playfair Display", serif;
    font-weight: 400;
    font-size: 84px;
    line-height: 1;
    letter-spacing: 1px;
    color: var(--text-white);
  }
  .sign__phone-row {
    position: absolute;
    left: 0;
    right: 0;
    top: 163px;
    height: 40px;
  }
  .sign__rule {
    position: absolute;
    top: 16px;
    width: 160px;
    height: 1px;
    background: var(--frame-white);
  }
  .sign__rule--left { left: 116px; }
  .sign__rule--right { left: 560px; }
  .sign__phone {
    position: absolute;
    left: 0;
    right: 0;
    top: -6px;
    margin: 0;
    text-align: center;
    font-family: "Playfair Display", serif;
    font-weight: 400;
    font-size: 38px;
    line-height: 1;
    color: var(--text-white);
  }
</style>
</head>
<body>
  <main class="canvas">
    <section class="sign" aria-label="Gilt Corner shop sign">
      <div class="sign__pattern-band" role="img" aria-label="Black border scattered with small gold hearts"></div>
      <div class="sign__panel"></div>
      <h1 class="sign__name">GILT CORNER</h1>
      <div class="sign__phone-row">
        <span class="sign__rule sign__rule--left"></span>
        <p class="sign__phone">011-555-0142</p>
        <span class="sign__rule sign__rule--right"></span>
      </div>
    </section>
  </main>
</body>
</html>
```